Premium website for 'Kestrel Voyages Elite'

Exclusive Torque League travel packages: world-class tickets, premium hospitality, seamless travel, and curated experiences that bring the spirit of each destination to life.

1. Overall Style and Impression
Aesthetic: Modern, premium, and dynamic, reflecting the speed and excitement of a high-profile sport or event.

Focus: Highly visual and focused on driving users toward specific, high-value conversion points (like finding a race or viewing a premium package).

We need on the homepage a few blocks for all destinations.
One the specific page of the destination, we need a list of tickets.
An example for our website is https://zomerratours.com/

Functional requirements

The web site is designed to deliver an end-to-end Torque League travel experience, combining flight bookings, hotel reservations, and race ticket purchases into one seamless booking process. This system provides a unified API layer that integrates external booking services and enables developers to build, manage, and customize complete travel packages for each TL Grand Prix event.

System Overview

The platform is built around three core microservices, all connected through a central Package API:

1. Flight Booking Service ✈️
Integrates with global flight providers (e.g.,Flyvora API).

2. Hotel Booking Service 🏨
Connects to hotel aggregator APIs (e.g., Bunkly).
Offers real-time availability, dynamic pricing, and filtering by proximity to TL circuits.

3. Ticket Booking Service 🎟️
Manages TL race ticket inventory and seat categories (Grandstand, VIP, General Admission).

CUSTOMER FEEDBACK
After each booking, a customer will be asked to fill in a questionaire.

CHAT BOT
A chat bot will answer the frequently asked questions.

OUR VISION
We believe life is meant to be lived at full throttle.
Not just seen, but felt. Not just remembered, but relived again and again.

MISSION
That’s why we craft once-in-a-lifetime Torque League journeys — where the roar of the engines meets the soul of the city. Where luxury travel and local culture collide with pure adrenaline. Where you don’t just watch the race… you become part of its story.

PRODUCTS

Target Market(s)

Affluent individuals, typically 35−65 years old, in professional, executive, or entrepreneurial roles. High net worth with significant disposable income.

Coding

Coded - Design and coding required

Number of Pages Required

5+ page

Requirements
Must have
• Central Package API
Nice to have
• Customer feedback after each booking , chat bot.

```html
<!DOCTYPE html>
<html lang="en">
<head>
<meta charset="utf-8">
<title>Kestrel Voyages Elite</title>
<link href="https://fonts.googleapis.com/css2?family=Poppins:wght@400;500;600&display=swap" rel="stylesheet">
<style>
:root{
  --red:#e01b24;
  --black:#000;
  --white:#fff;
  --ink:#111;
  --muted:#555;
  --line:#d9d9d9;
  --yellow:#ffd400;
}
*{margin:0;padding:0;box-sizing:border-box}
html,body{width:1200px;height:2678px;overflow:hidden}
body{font-family:"Poppins",sans-serif;color:var(--ink);background:var(--white)}
a{color:inherit;text-decoration:none}
.wrap{width:1080px;margin:0 auto;position:relative}

/* header */
.topbar{height:83px;background:var(--black);color:var(--white)}
.topbar .wrap{height:83px;display:flex;align-items:center}
.brand{font-size:24px;font-weight:600;letter-spacing:.2px;white-space:nowrap}
.search{margin-left:auto;width:203px;height:42px;border-bottom:1px solid #777;display:flex;align-items:center;justify-content:space-between;padding:0 4px;font-size:13px;color:#aaa}
.btn-login,.btn-register{height:42px;display:flex;align-items:center;justify-content:center;font-size:15px;font-weight:500;text-transform:uppercase}
.btn-login{width:115px;border:1px solid var(--white);margin-left:31px}
.btn-register{width:135px;background:var(--red);margin-left:15px}
.mainnav{height:37px;background:var(--red);color:var(--white);font-size:13px}
.mainnav .wrap{height:37px;display:flex;align-items:center}
.mainnav .links a{margin-right:56px}
.mainnav .links a.active{color:var(--yellow)}
.mainnav .right{margin-left:auto;display:flex;align-items:center;gap:6px}
.buy{color:var(--yellow);font-weight:500;display:flex;align-items:center;gap:8px;margin-right:22px}
.lang b{font-weight:600}
.lang span{opacity:.7;margin:0 6px}

/* hero */
.hero{height:555px;position:relative;color:var(--white);overflow:hidden}
.hero-photo{position:absolute;inset:0;background:radial-gradient(ellipse at 68% 62%,#b3241f 0%,#5a1512 22%,#232a33 52%,#11161d 100%)}
.hero-shade{position:absolute;inset:0;background:linear-gradient(90deg,rgba(0,0,0,.75) 0%,rgba(0,0,0,.35) 45%,rgba(0,0,0,0) 70%)}
.hero-copy{position:absolute;left:60px;top:118px;width:364px}
.hero-copy h1{font-size:48px;font-weight:600;line-height:1.05;color:var(--red);white-space:nowrap}
.hero-copy h1 span{display:block;color:var(--white);font-weight:400;font-size:40px;margin-top:6px}
.hero-copy hr{border:0;border-top:1px solid rgba(255,255,255,.55);margin:26px 0 24px}
.hero-copy p{font-size:14.5px;line-height:23px;font-weight:500}
.btn-red{display:inline-flex;align-items:center;gap:16px;background:var(--red);color:var(--white);font-size:15px;font-weight:500;text-transform:uppercase;padding:0 18px;height:41px}
.hero-copy .btn-red{margin-top:32px}
.slider{position:absolute;right:60px;top:478px;display:flex;flex-direction:column;align-items:flex-end}
.slider-count{font-size:32px;font-weight:500;line-height:40px}
.slider-bars{display:flex;gap:3px;margin-top:5px}
.slider-bars i{width:16px;height:4px;background:rgba(255,255,255,.5)}
.slider-bars i:first-child{background:var(--white)}

/* featured */
.section-title{text-align:center;font-size:33px;font-weight:600}
.featured{padding-top:74px;height:659px}
.cards{display:flex;gap:14px;margin-top:36px}
.dest-card{width:351px;height:436px;border:1px solid var(--line)}
.dest-img{height:214px}
.dest-body{padding:22px 26px}
.dest-body h3{font-size:17px;font-weight:500;white-space:nowrap}
.dest-date{display:flex;align-items:center;gap:9px;font-size:13px;color:var(--muted);margin:14px 0 8px}
.dest-body p{font-size:13px;line-height:21px;color:var(--muted);height:63px;white-space:nowrap}
.dest-body .btn-red{margin-top:16px}

/* about */
.about{height:468px;background:#050505;position:relative;color:var(--white);overflow:hidden}
.about-photo{position:absolute;left:0;top:0;width:820px;height:100%;background:radial-gradient(ellipse at 40% 60%,#9c2a12 0%,#4a1a10 28%,#1c1a1a 55%,#050505 85%)}
.about-copy{position:absolute;left:767px;top:70px;width:372px}
.about-copy h2{font-size:33px;font-weight:600;margin-bottom:16px;white-space:nowrap}
.about-copy p{font-size:13px;line-height:21px;margin-bottom:8px}
.about-copy .btn-red{margin-top:18px}

/* tickets */
.tickets{padding-top:84px;height:582px}
.ticket-grid{display:flex;gap:15px;margin-top:36px}
.ticket{width:259px;text-align:center}
.ticket-img{height:187px}
.ticket h3{font-size:17px;font-weight:500;line-height:24px;margin-top:24px;height:48px;white-space:nowrap}
.price{font-size:14px;color:#444;margin-top:10px}
.price span{margin-left:6px}
.qty{display:flex;justify-content:center;align-items:center;gap:14px;margin-top:12px;font-size:16px}
.qty i{width:20px;height:20px;border:1px solid #999;border-radius:50%;display:flex;align-items:center;justify-content:center;font-style:normal;font-size:14px;color:#666;line-height:1}
.add{display:flex;align-items:center;justify-content:center;height:38px;background:var(--red);color:var(--white);font-size:15px;font-weight:500;margin-top:14px;text-transform:uppercase}

/* footer */
.footer{height:294px;background:var(--black);color:var(--white);text-align:center;padding-top:46px}
.footer h2{font-size:44px;font-weight:600}
.footer p{font-size:12.5px;line-height:23px;width:480px;margin:16px auto 0}
.footer nav{font-size:12px;margin-top:18px}
.footer nav span{margin:0 14px}
.footer .rule{border-top:1px solid #333;width:1080px;margin:32px auto 0}
.footer small{display:block;font-size:11.5px;margin-top:14px}
</style>
</head>
<body>

<header class="topbar">
  <div class="wrap">
    <div class="brand">Kestrel Voyages Elite</div>
    <div class="search">Search
      <svg width="16" height="16" viewBox="0 0 16 16" fill="none" stroke="#aaa" stroke-width="1.5"><circle cx="7" cy="7" r="5.5"/><path d="M11 11l4 4"/></svg>
    </div>
    <a class="btn-login" href="#">Login</a>
    <a class="btn-register" href="#">Register</a>
  </div>
</header>

<nav class="mainnav">
  <div class="wrap">
    <div class="links">
      <a class="active" href="#">Home</a><a href="#">Destinations</a><a href="#">Packages</a><a href="#">About</a><a href="#">Contact Us</a>
    </div>
    <div class="right">
      <span class="buy">
        <svg width="16" height="14" viewBox="0 0 16 14" fill="none" stroke="#ffd400" stroke-width="1.6"><path d="M1 7l6-6 2 2a1.5 1.5 0 002 2l2 2-6 6-2-2a1.5 1.5 0 00-2-2z"/></svg>
        BUY TICKETS</span>
      <span class="lang"><b>EN</b><span>|</span>FR</span>
    </div>
  </div>
</nav>

<section class="hero">
  <div class="hero-photo" role="img" aria-label="Red racing car cornering on a circuit at dusk with blurred grandstands"></div>
  <div class="hero-shade"></div>
  <div class="hero-copy">
    <h1>Kestrel Voyages<span>Elite</span></h1>
    <hr>
    <p>Discover the thrill of Torque League in the world’s most iconic cities. Each destination offers exclusive race packages, luxury hospitality, and unforgettable cultural experiences.</p>
    <a class="btn-red" href="#">Explore Packages</a>
  </div>
  <div class="slider">
    <div class="slider-count">1/5</div>
    <div class="slider-bars"><i></i><i></i><i></i><i></i><i></i></div>
  </div>
</section>

<section class="featured">
  <div class="wrap">
    <h2 class="section-title">Featured Destinations</h2>
    <div class="cards">
      <article class="dest-card">
        <div class="dest-img" role="img" aria-label="Harbour street circuit lined with crowded grandstands and hillside buildings" style="background:linear-gradient(160deg,#8a9aa6,#6a5b55 45%,#3c3f4a)"></div>
        <div class="dest-body">
          <h3>Portvale Grand Prix</h3>
          <div class="dest-date"><svg width="14" height="13" viewBox="0 0 14 13" fill="none" stroke="#777"><rect x=".5" y="1.5" width="13" height="11"/><path d="M.5 4.5h13"/></svg>May 22–25, 2025</div>
          <p>Witness the world’s most glamorous<br>race from trackside terraces and<br>superyachts.</p>
          <a class="btn-red" href="#">View Packages <svg width="13" height="13" viewBox="0 0 13 13" fill="none" stroke="#fff" stroke-width="1.8"><path d="M2 11L11 2M4 2h7v7"/></svg></a>
        </div>
      </article>
      <article class="dest-card">
        <div class="dest-img" role="img" aria-label="Green racing car in the pit lane in front of team garages" style="background:linear-gradient(170deg,#c9cdd1,#7e858a 50%,#2f3b3a)"></div>
        <div class="dest-body">
          <h3>Sahrani Grand Prix</h3>
          <div class="dest-date"><svg width="14" height="13" viewBox="0 0 14 13" fill="none" stroke="#777"><rect x=".5" y="1.5" width="13" height="11"/><path d="M.5 4.5h13"/></svg>Dec 5–7, 2025</div>
          <p>A spectacular season finale under the lights —<br>luxury meets adrenaline.</p>
          <a class="btn-red" href="#">View Packages <svg width="13" height="13" viewBox="0 0 13 13" fill="none" stroke="#fff" stroke-width="1.8"><path d="M2 11L11 2M4 2h7v7"/></svg></a>
        </div>
      </article>
      <article class="dest-card">
        <div class="dest-img" role="img" aria-label="Night circuit beside an illuminated neon sphere" style="background:radial-gradient(ellipse at 55% 35%,#c43a8a,#3a2a9a 45%,#0d1030 85%)"></div>
        <div class="dest-body">
          <h3>Neon Mesa Grand Prix</h3>
          <div class="dest-date"><svg width="14" height="13" viewBox="0 0 14 13" fill="none" stroke="#777"><rect x=".5" y="1.5" width="13" height="11"/><path d="M.5 4.5h13"/></svg>Nov 20–23, 2025</div>
          <p>Experience the newest and most<br>electric race weekend on the TL<br>calendar.</p>
          <a class="btn-red" href="#">View Packages <svg width="13" height="13" viewBox="0 0 13 13" fill="none" stroke="#fff" stroke-width="1.8"><path d="M2 11L11 2M4 2h7v7"/></svg></a>
        </div>
      </article>
    </div>
  </div>
</section>

<section class="about">
  <div class="about-photo" role="img" aria-label="Orange racing car speeding with motion blur in dark light"></div>
  <div class="about-copy">
    <h2>About Kestrel</h2>
    <p>Lorem Ipsum has been the industry's standard dummy text ever since the 1500s, when an unknown printer took a galley of type and scrambled it to make a type specimen book. It has survived not only five centuries, but also the leap into electronic typesetting.</p>
    <p>Lorem Ipsum has been the industry's standard dummy text ever since the 1500s, when an unknown printer took a galley of type and scrambled it to make a type specimen book.</p>
    <a class="btn-red" href="#">Explore Packages</a>
  </div>
</section>

<section class="tickets">
  <div class="wrap">
    <h2 class="section-title">Available Ticket</h2>
    <div class="ticket-grid">
      <article class="ticket">
        <div class="ticket-img" role="img" aria-label="Main grandstand at night with fireworks" style="background:linear-gradient(180deg,#0c1430,#5a1f1a 60%,#1f6b2e)"></div>
        <h3>Silverline Silver Main<br>Grandstand 3-Days</h3>
        <div class="price">€1.769,01<span>EUR</span></div>
        <div class="qty"><i>−</i>0<i>+</i></div>
        <a class="add" href="#">Add to Card</a>
      </article>
      <article class="ticket">
        <div class="ticket-img" role="img" aria-label="Race start on a grid beside packed orange stands" style="background:linear-gradient(180deg,#a9b8c8,#7a7f80 40%,#5a8a4a)"></div>
        <h3>Harlow Reyes<br>Grandstand 3-Days</h3>
        <div class="price">€985,59<span>EUR</span></div>
        <div class="qty"><i>−</i>0<i>+</i></div>
        <a class="add" href="#">Add to Card</a>
      </article>
      <article class="ticket">
        <div class="ticket-img" role="img" aria-label="Racing cars on track past trackside barriers" style="background:linear-gradient(180deg,#8c9a9a,#6b7072 50%,#4f6a3f)"></div>
        <h3>Orbitel Sphere<br>Grandstands 3-Days</h3>
        <div class="price">€1.213,03<span>EUR</span></div>
        <div class="qty"><i>−</i>0<i>+</i></div>
        <a class="add" href="#">Add to Card</a>
      </article>
      <article class="ticket">
        <div class="ticket-img" role="img" aria-label="Podium ceremony with three drivers and national flags" style="background:linear-gradient(180deg,#c23b3b,#2f7a3a 30%,#1f5a2a)"></div>
        <h3>Orbitel Sphere<br>Grandstands Middle Rows</h3>
        <div class="price">€1.288,85<span>EUR</span></div>
        <div class="qty"><i>−</i>0<i>+</i></div>
        <a class="add" href="#">Add to Card</a>
      </article>
    </div>
  </div>
</section>

<footer class="footer">
  <h2>Kestrel Voyages Elite</h2>
  <p>Discover the thrill of Torque League in the world’s most iconic cities. Each destination offers exclusive race packages, luxury hospitality, and unforgettable cultural experiences.</p>
  <nav><a href="#">Home</a><span>|</span><a href="#">Destinations</a><span>|</span><a href="#">Packages</a><span>|</span><a href="#">About Us</a><span>|</span><a href="#">Contact Us</a></nav>
  <div class="rule"></div>
  <small>© 2025 Kestrel Voyages Elite – All Rights Reserved</small>
</footer>

</body>
</html>
```